Packaging design for aloe lotion bottle for a Laser Clinic

We need a packaging design for a body lotion bottle. Our business is a laser clinic and we are looking at slowly rolling out a range of skincare products. This lotion bottle is the first item with more to follow so the winning designer will have other designs to work on in the future.

The design needs to be classy, elegant, strong and sophisticated. The bottle will be clear with a shiny silver sleeved lid. The lotion itself, which will be visible through the bottle, will be a very light green colour. Think Mirelle Vantrau and Doriva as that is the image I want to convey.

Ideally we were thinking of having a design with a single colour but if you come up with a fantastic multi colour design that we love then we're open to it.

Reason: I have extended the deadline as I feel I need more time to allow designers to submit their designs. I haven't found a design that I love just yet. The project has been made a guaranteed payment upon completion. Thank you.

Target Market(s)

upper class high income earners with a high disposable income. People that look after themselves

Industry/Entity Type

Beauty Salon

Colors
000000
cadf82

Requirements
Must have
• must include the details below:
• After Beam Soothing Balm
• This soothing and calming anti inflammatory cream is specifically formulated for use after post laser treatments.
• Fresh Cucumber, Melon and Aloe Vera Leaf Juice blend together in perfect harmony to quickly cool you skin and restore your skins natural moisture.
• Our luxurious calming cream targets redness and helps to reduce inflammation, bringing you supple and radiant skin like never before.
• Directions: Use a liberal amount twice daily on all your treatment areas. This nourishing cream can also be used daily to restore moisture and softness to areas of the face and body not being treated by laser or IPL.
• Ingredients: water (aqua), glycine soja (soybean) oil, cetyl alcohol, glycerin dimethicone, butyrospermum parkii (shea butter), theobroma cacao (cocoa) seed butter, aloe barbadensis (aloe vera) leaf juice, tocopheryl acetate, sodium ascorbyl phosphate, disodium EDTA, ceteareth-20, carbomer, BHT, benzyl benzoate, butylphenyl methylpropional, hexyl cinnamal, linalool, glyceryl caprylate, methylisothiazolinone. May contain: Red 4 (CI 14700, aka 504), Yellow 5 (CI 19140, Ki4), Yellow 6 (CI 15985, KI5), Blue 1 (CI 42090, Ao1), Red 33 (CI 17200, Aka 227), Ext. Violet 2 (CI 60730, Murasaki401), Green 3 (CI 42053, Midori3)
• Against Animal Testing
• Manufactured in Australia
• www.velvetbloomclinic.example.com.au
• 500ml
• Pure Glow Laser Hair Removal logo (see attached files)
Nice to have
• A sophisticated and elegant design
Should not have
• no photos. not too many different colours

```html
<!DOCTYPE html>
<html lang="en">
<head>
<meta charset="utf-8">
<title>Pure Glow Body Lotion Label</title>
<link rel="stylesheet" href="https://fonts.googleapis.com/css2?family=Montserrat:wght@400&family=Oswald:wght@400&family=Libre+Caslon+Text&display=swap">
<style>
  :root {
    --backdrop: #e9e8e9;
    --label-green: #dcedd0;
    --ink: #3a3d3a;
    --ink-soft: #4a4d4a;
    --pattern-tone: #c6d8b9;
  }
  html, body {
    margin: 0;
    padding: 0;
    width: 1010px;
    height: 1200px;
    overflow: hidden;
    background: var(--backdrop);
  }
  .canvas {
    position: relative;
    width: 1010px;
    height: 1200px;
  }
  .label {
    position: absolute;
    left: 360px;
    top: 352px;
    width: 290px;
    height: 598px;
    background: var(--label-green);
    border-radius: 14px;
    color: var(--ink);
    text-align: center;
  }
  .brand {
    position: absolute;
    left: 0;
    right: 0;
    top: 74px;
    font-family: "Montserrat", sans-serif;
    font-weight: 400;
    color: var(--ink);
  }
  .brand-name {
    display: block;
    font-size: 38px;
    line-height: 40px;
    letter-spacing: -1px;
  }
  .brand-line {
    display: block;
    margin-top: 6px;
    font-size: 13.5px;
    letter-spacing: 1.6px;
  }
  .pattern-band {
    position: absolute;
    left: 5px;
    top: 181px;
    width: 280px;
    height: 124px;
    background: var(--pattern-tone);
  }
  .product-title {
    position: absolute;
    left: 0;
    right: 0;
    top: 354px;
    margin: 0;
    font-family: "Oswald", sans-serif;
    font-weight: 400;
    font-size: 26px;
    letter-spacing: 4px;
    line-height: 34px;
    color: var(--ink);
  }
  .product-subtitle {
    position: absolute;
    left: 0;
    right: 0;
    top: 394px;
    margin: 0;
    font-family: "Libre Caslon Text", serif;
    font-size: 14.5px;
    line-height: 20px;
    color: var(--ink-soft);
  }
  .divider {
    position: absolute;
    left: 122px;
    top: 423px;
    width: 46px;
    height: 1px;
    background: var(--ink);
  }
  .benefits {
    position: absolute;
    left: 0;
    right: 0;
    top: 437px;
    margin: 0;
    font-family: "Libre Caslon Text", serif;
    font-size: 11px;
    line-height: 14px;
    color: var(--ink-soft);
  }
  .directions {
    position: absolute;
    left: 0;
    right: 0;
    top: 484px;
    margin: 0;
    font-family: "Montserrat", sans-serif;
    font-size: 12.5px;
    line-height: 18px;
    color: var(--ink);
  }
  .volume {
    position: absolute;
    left: 0;
    right: 0;
    top: 517px;
    margin: 0;
    font-family: "Montserrat", sans-serif;
    font-size: 12px;
    line-height: 18px;
    color: var(--ink);
  }
</style>
</head>
<body>
  <main class="canvas">
    <section class="label">
      <div class="brand">
        <span class="brand-name">PURE GLOW</span>
        <span class="brand-line">LASER HAIR REMOVAL</span>
      </div>
      <div class="pattern-band" role="img" aria-label="Decorative band of outlined circles in rows flanked by dotted lines"></div>
      <h1 class="product-title">BODY LOTION</h1>
      <p class="product-subtitle">after beam soothing balm</p>
      <div class="divider"></div>
      <p class="benefits">targets redness<br>reduces inflammation</p>
      <p class="directions">use twice daily</p>
      <p class="volume">500ml</p>
    </section>
  </main>
</body>
</html>
```